Web app with questionnaires and graphs

For crewlifters.nl I want a clean design with good UX . It's a web app that let's users fill in questionnaires to assess things like team culture, psychological safety and so on. Colorwise should work with the Velmor Institute green logo. The app displays graphs (bar, line, pie) so these should also be incorporated.

```html
<!DOCTYPE html>
<html lang="en">
<head>
<meta charset="utf-8">
<title>Crew Lifters – Free Tools to Strengthen Your Teams</title>
<link href="https://fonts.googleapis.com/css2?family=Nunito:wght@400;600;700&display=swap" rel="stylesheet">
<style>
  :root {
    --green: #19b52f;
    --green-soft: #d3f1dc;
    --purple: #7f5bd5;
    --ink: #111111;
    --text: #444444;
    --muted: #777777;
    --line: #e2e2e2;
    --white: #ffffff;
  }
  * { margin: 0; padding: 0; box-sizing: border-box; }
  html, body { width: 1200px; height: 3215px; overflow: hidden; }
  body { position: relative; background: var(--white); font-family: "Nunito", sans-serif; color: var(--text); }
  .abs { position: absolute; }

  /* Header */
  .site-header { left: 0; top: 0; width: 1200px; height: 75px; background: var(--white); box-shadow: 0 2px 6px rgba(0,0,0,0.08); }
  .brand { line-height: 1; color: var(--ink); font-weight: 700; }
  .brand-name { font-size: 15px; letter-spacing: 0.2px; }
  .brand-by { font-size: 10px; font-weight: 700; margin-top: 3px; padding-left: 45px; }
  .main-nav a { position: absolute; top: 27px; font-size: 17px; color: #222; text-decoration: none; }
  .nav-active { position: absolute; left: 546px; top: 71px; width: 56px; height: 3px; background: var(--green); }

  /* Hero */
  .hero-title { left: 102px; top: 202px; font-size: 46px; font-weight: 700; line-height: 47px; color: var(--ink); }
  .hero-title .accent { color: var(--green); }
  .rule { height: 3px; width: 82px; }
  .rule-green { background: var(--green); }
  .rule-purple { background: var(--purple); }
  .lead { font-size: 18.5px; line-height: 28px; color: var(--text); }
  .btn { display: flex; align-items: center; justify-content: center; gap: 10px; height: 54px; font-size: 18.5px; font-weight: 700; color: var(--white); text-decoration: none; }
  .btn-green { background: var(--green); }
  .btn-purple { background: var(--purple); }
  .btn-white { background: var(--white); color: #333; font-weight: 600; }
  .art { border-radius: 48% 52% 45% 55% / 55% 45% 55% 45%; }

  /* Intro band */
  .intro-band { left: 0; top: 651px; width: 1200px; height: 578px; background: var(--purple); }
  .scroll-cue { left: 573px; top: 613px; width: 76px; height: 76px; border-radius: 50%; background: var(--white); box-shadow: 0 3px 10px rgba(0,0,0,0.18); display: flex; align-items: center; justify-content: center; z-index: 2; }
  .intro-art { left: 133px; top: 790px; width: 298px; height: 298px; border-radius: 50%; background: radial-gradient(circle at 50% 50%, #fbe9d3 0 30%, #ffffff 31%); }
  .intro-text { left: 536px; top: 810px; width: 508px; font-size: 20px; line-height: 28px; color: var(--white); }

  /* Tool sections */
  .tool-title { font-size: 46px; font-weight: 700; color: var(--ink); line-height: 56px; white-space: nowrap; }

  /* Footer */
  .footer-rule { left: 0; top: 2821px; width: 1200px; height: 3px; background: var(--line); }
  .footer-head { font-size: 20px; font-weight: 600; color: var(--muted); }
  .footer-list { list-style: none; font-size: 20px; line-height: 26px; color: var(--muted); }
  .social { display: flex; gap: 15px; }
  .social span { width: 28px; height: 28px; border-radius: 50%; background: #5c5c5c; }
  .legal-bar { left: 0; top: 3170px; width: 1200px; height: 45px; background: #e6e6e6; font-size: 17.5px; color: var(--muted); }
  .legal-bar p { position: absolute; top: 13px; }
</style>
</head>
<body>

<header class="site-header abs">
  <div class="brand abs" style="left:112px; top:24px;">
    <div class="brand-name">CREW LIFTERS</div>
    <div class="brand-by">by Velmor Institute</div>
  </div>
  <nav class="main-nav">
    <a href="#" style="left:551px;">Home</a>
    <a href="#" style="left:646px;">Features</a>
    <a href="#" style="left:761px;">Tools&nbsp;<svg width="12" height="8" viewBox="0 0 12 8"><path d="M1 1l5 5 5-5" fill="none" stroke="#333" stroke-width="1.5"/></svg></a>
    <a href="#" style="left:851px;">About Us</a>
    <a href="#" style="left:973px;">Feedback</a>
  </nav>
  <div class="nav-active"></div>
</header>

<section class="hero">
  <h1 class="hero-title abs">Free Tools to Strengthen<br>Your <span class="accent">Teams</span></h1>
  <div class="rule rule-green abs" style="left:100px; top:322px;"></div>
  <p class="lead abs" style="left:100px; top:351px;">Tools that help your teams further.<br>Need more help? We are happy to help you.</p>
  <a class="btn btn-green abs" href="#" style="left:100px; top:433px; width:230px;">Get Started Now
    <svg width="30" height="12" viewBox="0 0 30 12"><path d="M0 6h27M22 1l6 5-6 5" fill="none" stroke="#fff" stroke-width="2"/></svg></a>
  <div class="art abs" role="img" aria-label="Illustration of teammates helping each other climb onto rising blocks, with plants" style="left:525px; top:250px; width:522px; height:240px; background:linear-gradient(135deg,#e4f6e8,#d3f1dc 60%,#b9a4ea);"></div>
</section>

<div class="scroll-cue abs" aria-hidden="true">
  <svg width="20" height="32" viewBox="0 0 20 32"><path d="M10 2v27M3 22l7 7 7-7" fill="none" stroke="#666" stroke-width="2"/></svg>
</div>

<section class="intro-band abs"></section>
<div class="intro-art abs" role="img" aria-label="Illustration of hands filling in a checklist on a clipboard"></div>
<p class="intro-text abs">To make your team - and organization - better, you first need to map out how things are now. Our tools give you insight into the health of your team and the culture of the organization. With the results in hand, you can start improving your team and your organization. Each tool gives you useful tips and tricks to make improvements. Are you stuck? We are happy to help you!</p>
<a class="btn btn-white abs" href="#" style="left:536px; top:1042px; width:255px;">Start Questionnaire
  <svg width="30" height="12" viewBox="0 0 30 12"><path d="M0 6h27M22 1l6 5-6 5" fill="none" stroke="#333" stroke-width="2"/></svg></a>

<section class="tool">
  <h2 class="tool-title abs" style="left:97px; top:1412px;">Psychological safety</h2>
  <div class="rule rule-purple abs" style="left:100px; top:1497px;"></div>
  <p class="lead abs" style="left:100px; top:1525px; width:420px;">Measure the psychological safety in your team completely anonymously.</p>
  <a class="btn btn-purple abs" href="#" style="left:100px; top:1607px; width:255px;">Start Questionnaire
    <svg width="30" height="12" viewBox="0 0 30 12"><path d="M0 6h27M22 1l6 5-6 5" fill="none" stroke="#fff" stroke-width="2"/></svg></a>
  <div class="art abs" role="img" aria-label="Illustration of three colleagues assembling a green cube on a wall" style="left:640px; top:1374px; width:335px; height:294px; background:var(--green-soft);"></div>
</section>

<section class="tool">
  <div class="art abs" role="img" aria-label="Illustration of two colleagues shaking hands in an office with a desk and armchair" style="left:100px; top:1895px; width:406px; height:256px; background:linear-gradient(90deg,#bfeecb,#d3f1dc 60%,#c9ccd6);"></div>
  <h2 class="tool-title abs" style="left:553px; top:1887px;">Harland Culture Scan</h2>
  <div class="rule rule-purple abs" style="left:554px; top:1967px;"></div>
  <p class="lead abs" style="left:554px; top:1995px; width:460px;">With this tool you visualize the general culture of your organization. Is it mainly a Control, Competence, Collaboration or Cultivation culture?</p>
  <a class="btn btn-purple abs" href="#" style="left:554px; top:2103px; width:255px;">Start Questionnaire
    <svg width="30" height="12" viewBox="0 0 30 12"><path d="M0 6h27M22 1l6 5-6 5" fill="none" stroke="#fff" stroke-width="2"/></svg></a>
</section>

<section class="tool">
  <h2 class="tool-title abs" style="left:97px; top:2399px;">Developer Culture Test</h2>
  <div class="rule rule-purple abs" style="left:100px; top:2485px;"></div>
  <p class="lead abs" style="left:100px; top:2512px; width:420px;">Measure the psychological safety in your team completely anonymously.</p>
  <a class="btn btn-purple abs" href="#" style="left:100px; top:2595px; width:255px;">Start Questionnaire
    <svg width="30" height="12" viewBox="0 0 30 12"><path d="M0 6h27M22 1l6 5-6 5" fill="none" stroke="#fff" stroke-width="2"/></svg></a>
  <div class="art abs" role="img" aria-label="Illustration of a developer at a desk surrounded by code windows" style="left:640px; top:2358px; width:322px; height:311px; background:linear-gradient(160deg,#d3f1dc,#bfeecb 55%,#d3f1dc);"></div>
</section>

<footer>
  <div class="footer-rule abs"></div>
  <div class="brand abs" style="left:100px; top:2930px;">
    <div class="brand-name" style="font-size:19px;">CREW LIFTERS</div>
    <div class="brand-by" style="font-size:12px; padding-left:60px;">by Velmor Institute</div>
  </div>
  <h3 class="footer-head abs" style="left:375px; top:2920px;">QUICK LINKS</h3>
  <ul class="footer-list abs" style="left:375px; top:2966px;">
    <li>Home</li><li>Tools</li><li>About Us</li><li>Feedback</li>
  </ul>
  <h3 class="footer-head abs" style="left:613px; top:2920px;">CONTACT US</h3>
  <ul class="footer-list abs" style="left:613px; top:2966px; line-height:20px;">
    <li>Dummy Address</li><li>Line 2</li><li>Line 3</li>
  </ul>
  <h3 class="footer-head abs" style="left:846px; top:2920px;">SOCIAL MEDIA</h3>
  <div class="social abs" style="left:847px; top:2975px;" aria-label="Social media links">
    <span></span><span></span><span></span><span></span><span></span>
  </div>
  <div class="legal-bar abs">
    <p style="left:100px;">Copyright © CREW LIFTERS</p>
    <p style="right:154px;">All Rights Reserved.</p>
  </div>
</footer>

</body>
</html>
```